cryotherapy business . Whole Body Cryotherapy, Localised Cryotherapy, Cryofacials

Need home page plus services, about, pricing, online booking, contact and blog page

I want something slick, hip and professional. Our studio colours are duck egg blue, white and grey

I would also like a social media scroll at the bottom of every page

I will upload some web designs that I like the look of

Target Market(s)

Men and Women 25-45

Industry/Entity Type

Health And Wellness

Coding

Coded - Design and coding required

Number of Pages Required

5+ page

Font styles to use
Serif
Sans Serif

Requirements
Must have
• Must be eye catching and easy to navigate
Nice to have
• animation
Should not have
• Not sure what the site should not have. I am fairly open to ideas as this is a brand new business.

```html
<!DOCTYPE html>
<html lang="en">
<head>
<meta charset="utf-8">
<title>Cryotherapy Business</title>
<link rel="stylesheet" href="https://fonts.googleapis.com/css2?family=Cinzel:wght@400;500&family=Lato:ital,wght@0,300;0,400;0,700;1,400&family=Roboto+Condensed:wght@700&display=swap">
<style>
:root{
  --duck:#a8cccc;
  --duck-deep:#8fb9ba;
  --duck-soft:#c4dcdc;
  --mist:#f2f7f7;
  --white:#ffffff;
  --ink:#2f3333;
  --grey:#5d6364;
  --line:#a9cfcd;
}
*{margin:0;padding:0;box-sizing:border-box}
html,body{width:1200px;height:4344px;overflow:hidden}
body{position:relative;background:var(--white);font-family:'Lato',sans-serif;color:var(--grey)}
.abs{position:absolute}
.center{left:0;width:1200px;text-align:center}
.serif{font-family:'Cinzel',serif;color:var(--ink);letter-spacing:1px}
.divider{position:absolute;height:3px;width:60px;background:var(--line)}
.divider.mid{left:570px}

/* header */
.site-header{position:absolute;top:0;left:0;width:1200px;height:93px;background:var(--white);box-shadow:0 2px 6px rgba(0,0,0,.12);z-index:3}
.nav-link{position:absolute;top:38px;font-size:14px;color:var(--grey);letter-spacing:.5px}
.nav-link.active{color:var(--duck-deep)}
.brand{position:absolute;left:0;width:1200px;text-align:center;font-family:'Lato',sans-serif;font-weight:400;font-size:21px;line-height:1;color:var(--duck-deep)}
.brand-mark{display:inline-block;width:10px;height:10px;border-radius:50%;background:currentColor;margin-right:9px;vertical-align:middle;position:relative;top:-2px}
.notch{position:absolute;left:560px;top:90px;z-index:4}

/* hero */
.hero{position:absolute;top:93px;left:0;width:1200px;height:581px}
.hero-title{position:absolute;top:480px;font-family:'Roboto Condensed',sans-serif;font-weight:700;font-size:62px;color:var(--white);letter-spacing:1px}

/* text */
.lead{font-style:italic;font-size:14.5px;line-height:27px;color:var(--grey)}
.body{font-size:13.5px;line-height:25.5px;color:var(--grey)}

/* services */
.band{position:absolute;left:0;width:1200px;background:var(--mist)}
.svc-icon{position:absolute;width:104px;height:104px;border-radius:50%;background:var(--white);box-shadow:0 6px 6px rgba(120,160,160,.35);display:flex;align-items:center;justify-content:center}
.svc-title{position:absolute;width:360px;text-align:center;font-size:20px;color:var(--ink)}
.svc-text{position:absolute;width:360px;text-align:center;font-size:13.5px;line-height:25px}

/* pricing */
.ring{position:absolute;border-radius:50%}
.price-badge{position:absolute;left:499px;top:1761px;width:88px;height:88px;border-radius:50%;background:var(--duck);color:var(--white);font-family:'Cinzel',serif;font-size:26px;display:flex;align-items:center;justify-content:center}

/* booking */
.btn{position:absolute;left:79px;top:2327px;width:186px;height:50px;border-radius:25px;background:var(--white);color:var(--duck-deep);font-family:'Cinzel',serif;font-size:16px;letter-spacing:1px;display:flex;align-items:center;justify-content:center;box-shadow:0 3px 6px rgba(0,0,0,.1)}

/* testimonial */
.quote-card{position:absolute;left:78px;top:2781px;width:551px;height:416px;background:var(--mist);border-radius:6px}
.dot{position:absolute;top:3109px;width:12px;height:12px;border-radius:50%;border:1.5px solid var(--duck)}
.dot.on{background:var(--duck)}

/* news */
.news-photo{position:absolute;top:3522px;width:269px;height:312px;border-radius:6px}
.news-card{position:absolute;top:3585px;width:269px;height:312px;background:var(--white);border-radius:6px;box-shadow:0 4px 14px rgba(110,150,150,.18);text-align:center}
.news-card h3{margin-top:70px;font-weight:400;font-size:19px;color:var(--ink)}
.news-card p{margin:14px 22px 0;font-size:13px;line-height:25px}
.news-card a{display:inline-block;margin-top:12px;font-size:13.5px;color:var(--ink);text-decoration:underline}

/* footer */
.site-footer{position:absolute;top:3988px;left:0;width:1200px;height:356px;background:var(--duck)}
.social{position:absolute;top:4122px;width:52px;height:52px;border-radius:50%;background:var(--white);display:flex;align-items:center;justify-content:center}
.foot-link{position:absolute;top:4209px;font-size:14px;color:var(--white)}
.copy{position:absolute;top:4302px;font-size:13.5px;color:var(--white)}
</style>
</head>
<body>

<header class="site-header">
  <span class="nav-link active" style="left:79px">HOME</span>
  <span class="nav-link" style="left:160px">SERVICES</span>
  <span class="nav-link" style="left:263px">ABOUT</span>
  <div class="brand" style="top:35px"><span class="brand-mark"></span>Frostline Studio</div>
  <span class="nav-link" style="left:881px">PRICING</span>
  <span class="nav-link" style="left:977px">BLOG</span>
  <span class="nav-link" style="left:1052px">CONTACT</span>
</header>
<svg class="notch" width="80" height="28" viewBox="0 0 80 28"><path d="M0 3 C20 3 24 25 40 25 C56 25 60 3 80 3 Z" fill="#fff" style="filter:drop-shadow(0 2px 2px rgba(0,0,0,.12))"/></svg>

<section class="hero">
  <svg width="1200" height="581" viewBox="0 0 1200 581" role="img" aria-label="Woman seen from behind surrounded by cold mist">
    <defs>
      <linearGradient id="heroFill" x1="0" y1="0" x2="0" y2="1">
        <stop offset="0" stop-color="#9fb9c6"/>
        <stop offset=".55" stop-color="#b8cbd5"/>
        <stop offset="1" stop-color="#d8e2e8"/>
      </linearGradient>
    </defs>
    <path d="M0 0 H1200 V514 Q600 650 0 514 Z" fill="url(#heroFill)"/>
  </svg>
  <div class="hero-title center">CRYOTHERAPY BUSINESS</div>
</section>

<section class="welcome">
  <h1 class="abs center serif" style="top:728px;font-size:30px;font-weight:400">WELCOME TO CRYOTHERAPY BUSINESS</h1>
  <div class="divider mid" style="top:784px"></div>
  <p class="abs center lead" style="top:814px">Lorem Ipsum is simply dummy text of the printing and typesetting industry. Lorem Ipsum<br>has been the industry's standard dummy text ever since the 1500s, when an unknown printer took a<br>galley of type and scrambled it to make a type specimen book.</p>
  <p class="abs center body" style="top:920px">It has survived not only five centuries, but also the leap into electronic typesetting, remaining essentially<br>unchanged. It was popularised in the 1960s with the release of Lettrafix sheets containing Lorem Ipsum passages,<br>and more recently with desktop publishing software like Pagecraft Studio including versions.</p>
</section>

<section class="band" style="top:1062px;height:468px"></section>
<section class="services">
  <h2 class="abs center serif" style="top:1120px;font-size:30px;font-weight:400">OUR SERVICES</h2>
  <div class="divider mid" style="top:1175px"></div>

  <div class="svc-icon" style="left:186px;top:1220px">
    <svg width="40" height="52" viewBox="0 0 40 52"><path d="M10 4 H30 V16 L20 22 L10 16 Z M10 26 L30 18 V28 L10 36 Z M14 40 L26 35 V42 L20 50 L14 44 Z" fill="#9cc4c5"/></svg>
  </div>
  <div class="svc-icon" style="left:548px;top:1220px">
    <svg width="50" height="52" viewBox="0 0 50 52"><rect x="12" y="12" width="26" height="34" rx="3" fill="none" stroke="#9cc4c5" stroke-width="3"/><circle cx="25" cy="7" r="4" fill="#9cc4c5"/><path d="M25 14 V44 M4 26 H46" stroke="#9cc4c5" stroke-width="3"/></svg>
  </div>
  <div class="svc-icon" style="left:909px;top:1220px">
    <svg width="52" height="44" viewBox="0 0 52 44"><path d="M4 30 C8 12 30 2 48 6 C46 24 32 38 12 38 Z" fill="none" stroke="#9cc4c5" stroke-width="3"/><path d="M14 30 C18 20 28 14 38 12" stroke="#9cc4c5" stroke-width="3" fill="none"/></svg>
  </div>

  <div class="svc-title" style="left:58px;top:1364px">Whole Body Cryotherapy</div>
  <div class="svc-title" style="left:420px;top:1364px">Localised Cryotherapy</div>
  <div class="svc-title" style="left:781px;top:1364px">Cryofacials</div>
  <p class="svc-text" style="left:58px;top:1407px">Lorem Ipsum is simply dummy text of the<br>printing and typesetting industry.</p>
  <p class="svc-text" style="left:420px;top:1407px">Lorem Ipsum is simply dummy text of the<br>printing and typesetting industry.</p>
  <p class="svc-text" style="left:781px;top:1407px">Lorem Ipsum is simply dummy text of the<br>printing and typesetting industry.</p>
</section>

<section class="pricing">
  <div class="ring" style="left:79px;top:1625px;width:364px;height:364px;background:#eef4f4"></div>
  <div class="ring" style="left:114px;top:1660px;width:294px;height:294px;background:linear-gradient(135deg,#7e9aa3,#e8eeee 45%,#8aa3aa)"></div>
  <div class="ring" role="img" aria-label="Localised cryotherapy treatment on a client's back" style="left:122px;top:1668px;width:278px;height:278px;background:linear-gradient(160deg,#b9d6d4,#a4c9c7)"></div>
  <div class="abs" style="left:122px;top:1777px;width:278px;text-align:center;font-family:'Cinzel',serif;font-size:22px;line-height:31px;color:var(--white)">LOCALISED<br>CRYOTHERAPY</div>
  <div class="ring" role="img" aria-label="Client in a cryotherapy chamber with blue light" style="left:456px;top:1611px;width:88px;height:88px;background:radial-gradient(circle at 55% 45%,#8fb3e6,#243d92 70%);border:2px solid #fff"></div>
  <div class="ring" role="img" aria-label="Client receiving a cryofacial" style="left:456px;top:1914px;width:88px;height:88px;background:radial-gradient(circle at 60% 55%,#d8c6bd,#2b4f8a 70%);border:2px solid #fff"></div>
  <div class="abs" style="left:447px;top:1805px;width:52px;border-top:1.5px dotted #b7d2d2"></div>
  <div class="price-badge">$50</div>

  <h2 class="abs serif" style="left:690px;top:1648px;font-size:30px;font-weight:400">THERAPY PRICING</h2>
  <div class="divider" style="left:692px;top:1705px"></div>
  <div class="abs" style="left:692px;top:1733px;font-size:18px;color:var(--grey)">Localised Cryotherapy</div>
  <p class="abs body" style="left:692px;top:1787px;width:440px">Lorem Ipsum is simply dummy text of the printing and typesetting industry. Lorem Ipsum has been the industry's standard dummy text ever since the 1500s, when an unknown printer took a galley of type and scrambled it to make a type specimen book.</p>
  <p class="abs body" style="left:692px;top:1903px;width:440px">It has survived not only five centuries, but also the leap into elect typesetting, remaining essentially unchanged It was popularised.</p>
</section>

<section class="booking">
  <svg class="abs" style="left:0;top:2090px" width="1200" height="446" viewBox="0 0 1200 446" role="img" aria-label="Woman relaxing in a cryotherapy chamber surrounded by mist">
    <defs>
      <linearGradient id="bookFill" x1="0" y1="0" x2="1" y2="0">
        <stop offset="0" stop-color="#a6caca"/>
        <stop offset=".6" stop-color="#b3d2d2"/>
        <stop offset="1" stop-color="#c5dcdc"/>
      </linearGradient>
    </defs>
    <path d="M0 42 Q600 -40 1200 38 V261 Q620 606 0 312 Z" fill="url(#bookFill)"/>
  </svg>
  <h2 class="abs serif" style="left:79px;top:2189px;font-size:30px;font-weight:400;color:var(--white);letter-spacing:2px">ONLINE BOOKING</h2>
  <p class="abs" style="left:79px;top:2247px;font-size:14.5px;line-height:27px;color:var(--white)">Lorem Ipsum is simply dummy text of the printing and<br>typesetting industry. Lorem Ipsum has been the industry's.</p>
  <div class="btn">BOOK NOW</div>
</section>

<section class="testimonials">
  <h2 class="abs center serif" style="top:2585px;font-size:30px;font-weight:400">CLIENT TESTIMONIALS</h2>
  <div class="divider mid" style="top:2642px"></div>
  <p class="abs center body" style="top:2668px">It has survived not only five centuries, but also the leap into elect typesetting,<br>remaining essentially unchanged It was popularised.</p>

  <div class="quote-card"></div>
  <svg class="abs" style="left:108px;top:2864px" width="84" height="84" viewBox="0 0 84 84"><circle cx="42" cy="42" r="40" fill="none" stroke="#a8cccc" stroke-width="2"/><path d="M26 48 Q26 34 36 30 V35 Q32 38 32 40 H37 V52 H26 Z M45 48 Q45 34 55 30 V35 Q51 38 51 40 H56 V52 H45 Z" fill="#a8cccc"/></svg>
  <p class="abs body" style="left:111px;top:2967px;width:420px;font-size:13.5px">Lorem Ipsum is simply dummy text of the printing and typesetting industry. Lorem Ipsum has been the industry unknown printer took a galley of type and scrambled.</p>
  <div class="abs" style="left:111px;top:3058px;font-size:13.5px;color:var(--ink)">- NAME SURNAME</div>
  <span class="dot on" style="left:112px"></span>
  <span class="dot" style="left:133px"></span>
  <span class="dot" style="left:154px"></span>
  <span class="dot" style="left:174px"></span>

  <div class="abs" role="img" aria-label="Smiling woman in a teal cryotherapy cabin" style="left:581px;top:2833px;width:541px;height:312px;border-radius:4px;background:linear-gradient(135deg,#7fd0d2,#35a7ad 55%,#1f7e86)"></div>
</section>

<section class="band" style="top:3290px;height:698px"></section>
<section class="news">
  <h2 class="abs center serif" style="top:3336px;font-size:30px;font-weight:400">LATEST NEWS</h2>
  <div class="divider mid" style="top:3394px"></div>
  <p class="abs center body" style="top:3420px">It has survived not only five centuries, but also the leap into elect typesetting,<br>remaining essentially unchanged It was popularised.</p>

  <div class="news-photo" role="img" aria-label="Woman in a blue-lit cryotherapy chamber with mist" style="left:78px;background:linear-gradient(160deg,#3d4fb3,#8aa0d8 50%,#2c3c96)"></div>
  <article class="news-card" style="left:307px">
    <h3>Lorem Ipsum is simply.</h3>
    <p>Lorem Ipsum is simply dummy text of the printing and typesetting industry. Lorem Ipsum has been the industry unknown printer took.</p>
    <a>READ MORE</a>
  </article>

  <div class="news-photo" role="img" aria-label="Man standing in a cryotherapy cabin with a timer display" style="left:624px;background:linear-gradient(170deg,#58b8ec,#a7dcf5 55%,#d9b49a)"></div>
  <article class="news-card" style="left:853px">
    <h3>Lorem Ipsum is simply.</h3>
    <p>Lorem Ipsum is simply dummy text of the printing and typesetting industry. Lorem Ipsum has been the industry unknown printer took.</p>
    <a>READ MORE</a>
  </article>
</section>

<footer class="site-footer"></footer>
<div class="brand" style="top:4060px;color:#fff"><span class="brand-mark"></span>Frostline Studio</div>

<a class="social" style="left:480px" aria-label="Share">
  <svg width="22" height="22" viewBox="0 0 22 22"><circle cx="5" cy="11" r="3" fill="#a8cccc"/><circle cx="17" cy="4.5" r="3" fill="#a8cccc"/><circle cx="17" cy="17.5" r="3" fill="#a8cccc"/><path d="M5 11 L17 4.5 M5 11 L17 17.5" stroke="#a8cccc" stroke-width="2"/></svg>
</a>
<a class="social" style="left:542px" aria-label="Email">
  <svg width="22" height="18" viewBox="0 0 22 18"><rect x="1" y="2" width="20" height="14" rx="2" fill="none" stroke="#a8cccc" stroke-width="2"/><path d="M1.5 3 L11 10 L20.5 3" fill="none" stroke="#a8cccc" stroke-width="2"/></svg>
</a>
<a class="social" style="left:604px" aria-label="Messages">
  <svg width="22" height="20" viewBox="0 0 22 20"><path d="M2 2 H20 V14 H9 L4 18 V14 H2 Z" fill="none" stroke="#a8cccc" stroke-width="2" stroke-linejoin="round"/></svg>
</a>
<a class="social" style="left:667px" aria-label="Phone">
  <svg width="20" height="20" viewBox="0 0 20 20"><path d="M4 1 L8 1 L9 6 L6.5 7.5 Q8.5 11.5 12.5 13.5 L14 11 L19 12 L19 16 Q19 19 16 19 Q1 17 1 4 Q1 1 4 1 Z" fill="#a8cccc"/></svg>
</a>

<span class="foot-link" style="left:390px">Home</span>
<span class="foot-link" style="left:455px">|</span>
<span class="foot-link" style="left:484px">About</span>
<span class="foot-link" style="left:550px">|</span>
<span class="foot-link" style="left:579px">Pricing</span>
<span class="foot-link" style="left:648px">|</span>
<span class="foot-link" style="left:677px">Blog</span>
<span class="foot-link" style="left:730px">|</span>
<span class="foot-link" style="left:759px">Contact</span>
<p class="copy center" style="left:0">2019 ©cryotherapy business - All Rights Reserved.</p>

</body>
</html>
```